" O Empório do Tavo era uma Distribuidora de Bebidas antigamente. O novo proprietário reformou o estabebecimento e quer se posicionar no mercado na lacuna entre uma simples distribuidora de bebidas e um empório mais chique. Nao é tao chique como um empório classe A, mas oferece mais de 400 tipos de cervejas importadas, cortes especiais de carne, dentre outros produtos. O foco é a venda de bebidas, principalmente cervejas. "

```html
<!DOCTYPE html>
<html lang="pt-BR">
<head>
<meta charset="utf-8">
<title>Cartão Fidelidade — Empório do Tavo</title>
<link rel="stylesheet" href="https://fonts.googleapis.com/css2?family=Cormorant+Garamond:wght@500;600&display=swap">
<style>
  :root {
    --backdrop: #ece6df;
    --wine: #7e1c2c;
    --wine-deep: #6c1524;
    --gold: #e6c78a;
    --field: #ffffff;
  }
  * { box-sizing: border-box; margin: 0; padding: 0; }
  html, body {
    width: 1200px;
    height: 1200px;
    overflow: hidden;
    background: var(--backdrop);
  }
  .card-set {
    width: 1200px;
    height: 1200px;
    display: flex;
    justify-content: center;
    align-items: center;
    gap: 70px;
  }
  .card {
    width: 440px;
    height: 580px;
    border-radius: 22px;
    background: var(--wine);
    font-family: "Cormorant Garamond", Georgia, serif;
    color: var(--gold);
    box-shadow: 0 10px 28px rgba(60, 20, 20, 0.18);
  }
  .card--front {
    display: flex;
    justify-content: center;
    align-items: center;
  }
  .brand-name {
    font-weight: 600;
    font-size: 52px;
    line-height: 1.05;
    text-align: center;
    color: var(--gold);
  }
  .card--back {
    display: flex;
    flex-direction: column;
    align-items: center;
    padding: 54px 40px 0;
  }
  .card-title {
    font-weight: 600;
    font-size: 36px;
    letter-spacing: 0.5px;
    margin-bottom: 56px;
  }
  .field-label {
    font-weight: 600;
    font-size: 28px;
    margin-bottom: 12px;
  }
  .field-box {
    width: 100%;
    height: 56px;
    border-radius: 10px;
    background: var(--field);
    margin-bottom: 40px;
  }
  .brand-name--small {
    margin-top: 28px;
    font-size: 32px;
  }
</style>
</head>
<body>
  <main class="card-set">
    <section class="card card--front" aria-label="Frente do cartão">
      <p class="brand-name">Empório<br>do Tavo</p>
    </section>
    <section class="card card--back" aria-label="Verso do cartão">
      <h1 class="card-title">Cartão Fidelidade</h1>
      <p class="field-label">Nome do cliente</p>
      <div class="field-box"></div>
      <p class="field-label">Código</p>
      <div class="field-box"></div>
      <p class="brand-name brand-name--small">Empório<br>do Tavo</p>
    </section>
  </main>
</body>
</html>
```